Pel'k Marrowind Travel

We need a sleek, professional, inviting card to elicit global travel for the experienced and professional traveler. Royal blue, black and silver. (perhaps the wording could be silver with black shadow?-get creative) Maybe a watermark on the front and the full raised logo on the back.
We want a stylish and modern card, but professional.

```html
<!DOCTYPE html>
<html lang="en">
<head>
<meta charset="utf-8">
<title>Pel'k Marrowind Travel — Business Card</title>
<link rel="stylesheet" href="https://fonts.googleapis.com/css2?family=Open+Sans:ital,wght@0,400;0,600;0,700;1,400&display=swap">
<style>
  :root {
    --stage: #2a2a2c;
    --card: #1b1b1c;
    --edge-blue: #1ea1dc;
    --name-blue: #27a6e0;
    --silver: #9a9a9c;
    --silver-line: #6f6f72;
    --text-grey: #c9c9cb;
    --muted-grey: #a8a8aa;
    --icon-green: #7cc242;
  }
  * { margin: 0; padding: 0; box-sizing: border-box; }
  html, body { width: 1200px; height: 900px; overflow: hidden; }
  body {
    background: var(--stage);
    font-family: "Open Sans", Arial, sans-serif;
    position: relative;
  }
  .card {
    position: absolute;
    left: 280px;
    width: 640px;
    height: 366px;
    background: var(--card);
    border-bottom: 6px solid var(--edge-blue);
    box-shadow: 0 14px 30px rgba(0,0,0,0.55);
    overflow: hidden;
  }
  .card--back { top: 67px; }
  .card--front { top: 467px; }

  /* Back: brand lockup */
  .brand {
    position: absolute;
    inset: 0;
    display: flex;
    flex-direction: column;
    align-items: center;
    justify-content: center;
    gap: 16px;
  }
  .brand__mark {
    width: 26px; height: 26px;
    border-radius: 50%;
    background: var(--silver);
  }
  .brand__name {
    color: var(--silver);
    font-weight: 600;
    font-size: 34px;
    letter-spacing: 4px;
    text-transform: uppercase;
  }
  .brand__rule {
    width: 380px;
    height: 1px;
    background: var(--silver-line);
  }

  /* Front: contact side */
  .person {
    position: absolute;
    right: 382px;
    top: 118px;
    text-align: right;
  }
  .person__name {
    color: var(--name-blue);
    font-weight: 700;
    font-size: 25px;
    letter-spacing: 0.5px;
    text-transform: uppercase;
    line-height: 1.1;
  }
  .person__title {
    color: var(--muted-grey);
    font-style: italic;
    font-size: 15px;
    margin-top: 4px;
  }
  .divider {
    position: absolute;
    left: 275px;
    top: 108px;
    width: 1px;
    height: 78px;
    background: var(--name-blue);
  }
  .contact {
    position: absolute;
    left: 296px;
    top: 112px;
    list-style: none;
  }
  .contact__item {
    display: flex;
    align-items: center;
    gap: 9px;
    color: var(--text-grey);
    font-size: 15px;
    line-height: 24px;
  }
  .contact__icon { width: 13px; height: 13px; flex: none; }
  .address {
    position: absolute;
    left: 0; right: 0;
    bottom: 62px;
    text-align: center;
    color: var(--text-grey);
    font-size: 15px;
    letter-spacing: 0.3px;
  }
</style>
</head>
<body>

<section class="card card--back" aria-label="Card back">
  <div class="brand">
    <span class="brand__mark" aria-hidden="true"></span>
    <div class="brand__name">Pel'k Marrowind Travel</div>
    <span class="brand__rule" aria-hidden="true"></span>
  </div>
</section>

<section class="card card--front" aria-label="Card front">
  <div class="person">
    <div class="person__name">Dorian Vell</div>
    <div class="person__title">President</div>
  </div>
  <span class="divider" aria-hidden="true"></span>
  <ul class="contact">
    <li class="contact__item">
      <svg class="contact__icon" viewBox="0 0 16 16" aria-hidden="true">
        <path fill="var(--icon-green)" d="M3.6 1.2l2.3 2.6c.4.4.3 1-.1 1.4L4.7 6.3c.8 1.9 2.9 4.1 4.9 5l1.1-1.1c.4-.4 1-.4 1.4-.1l2.6 2.3c.4.4.4 1 0 1.4l-1.3 1.3C11 16.5 0 6.3 1.1 2.5L2.3 1.2c.4-.4 1-.4 1.3 0z"/>
      </svg>
      555-013-4827
    </li>
    <li class="contact__item">
      <svg class="contact__icon" viewBox="0 0 16 16" aria-hidden="true">
        <rect x="1" y="3" width="14" height="10" rx="1" fill="var(--icon-green)"/>
        <path d="M1.5 4l6.5 5 6.5-5" fill="none" stroke="var(--card)" stroke-width="1.3"/>
      </svg>
      info@pelkmarrowind.com
    </li>
    <li class="contact__item">
      <svg class="contact__icon" viewBox="0 0 16 16" aria-hidden="true">
        <circle cx="8" cy="8" r="7" fill="var(--icon-green)"/>
        <ellipse cx="8" cy="8" rx="3" ry="7" fill="none" stroke="var(--card)" stroke-width="1"/>
        <path d="M1 8h14" stroke="var(--card)" stroke-width="1"/>
      </svg>
      www.pelkmarrowind.com
    </li>
  </ul>
  <p class="address">4817 Lantern Bay Wharf, Corvale CA 93100</p>
</section>

</body>
</html>
```